Car Wrap Design for Parquet Company

We are a parquet retailer and parquet laying company from Germany. We need a car wrap design for our van. It should have a noticeable design and so be modern and look premium. Enclosed we present you three favorite designs from other companys. We especially like favorite1. We like the theme wood in the design. We'd like to hear the follwing in the advertisement: - Over 25 years experience (more that 25 years of experience) - Birch to Wenge (our slogan) quality - www.Dielen-Warnke.example (our website) - 0913 - 72 15 904 (our telephone number) Our van is a Varlo K420 M3T3. Enclosed you find some pictures and the dimensions.
Colors
Designer to choose colors to be used in the design.
Look and feel
Each slider illustrates characteristics of the customer's brand and the style your logo design should communicate.

```html
<!DOCTYPE html>
<html lang="de">
<head>
<meta charset="utf-8">
<title>Dielen Warnke – Fahrzeugbeschriftung</title>
<link href="https://fonts.googleapis.com/css2?family=Baloo+2:wght@700;800&family=Saira:wght@600&display=swap" rel="stylesheet">
<style>
  :root {
    --bg: #ececec;
    --wood-light: #e9c998;
    --wood-mid: #d8ad72;
    --wood-dark: #c8975a;
    --ink-brown: #6b3a1f;
    --brand-orange: #e07a22;
    --trim-black: #2a2a2a;
    --glass: #4a5560;
    --tail-red: #c2262e;
    --tyre: #3a3a3a;
    --hub: #bfc3c7;
  }
  html, body { margin: 0; padding: 0; overflow: hidden; }
  body { width: 1200px; height: 800px; background: var(--bg); }
  .wrap-sheet { display: block; width: 1200px; height: 800px; }
  .tagline { font-family: "Baloo 2", sans-serif; font-weight: 800; fill: var(--ink-brown); }
  .contact { font-family: "Baloo 2", sans-serif; font-weight: 700; fill: var(--ink-brown); letter-spacing: 2px; }
  .brand-name { font-family: "Saira", sans-serif; font-weight: 600; fill: var(--brand-orange); }
  .seam { stroke: var(--wood-dark); stroke-width: 1; opacity: .6; }
  .trim { fill: var(--trim-black); }
  .glass { fill: var(--glass); }
  .tail-light { fill: var(--tail-red); }
  .social-dot { fill: none; stroke: var(--ink-brown); stroke-width: 2; }
</style>
</head>
<body>
<svg class="wrap-sheet" viewBox="0 0 1200 800" xmlns="http://www.w3.org/2000/svg">
  <defs>
    <linearGradient id="wood" x1="0" y1="0" x2="1" y2="1">
      <stop offset="0" stop-color="var(--wood-light)"/>
      <stop offset=".55" stop-color="var(--wood-mid)"/>
      <stop offset="1" stop-color="var(--wood-light)"/>
    </linearGradient>
  </defs>

  <!-- Front / hood panel -->
  <g class="panel-front">
    <path role="img" aria-label="Holzdielen-Optik als Fahrzeugfolie" fill="url(#wood)" d="M90,380 L90,240 Q95,150 150,120 L330,120 Q385,150 390,240 L390,380 Z"/>
    <path class="glass" d="M125,215 Q135,150 160,135 L320,135 Q345,150 355,215 Z"/>
    <line class="seam" x1="90" y1="270" x2="390" y2="270"/>
    <line class="seam" x1="90" y1="300" x2="390" y2="300"/>
    <rect x="110" y="242" width="16" height="16" fill="var(--ink-brown)"/>
    <text class="brand-name" x="134" y="257" font-size="18" letter-spacing="2">DIELEN WARNKE</text>
    <text class="contact" x="240" y="285" font-size="11" text-anchor="middle">WWW.DIELEN-WARNKE.EXAMPLE</text>
    <rect class="trim" x="90" y="320" width="300" height="60" rx="6"/>
    <rect x="150" y="330" width="180" height="30" rx="6" fill="#1c1c1c"/>
    <rect x="98" y="326" width="42" height="16" rx="4" fill="#d9dde0"/>
    <rect x="340" y="326" width="42" height="16" rx="4" fill="#d9dde0"/>
  </g>

  <!-- Side panel -->
  <g class="panel-side">
    <path role="img" aria-label="Holzdielen-Optik als Fahrzeugfolie" fill="url(#wood)" d="M470,385 L470,300 Q475,258 530,244 L620,170 Q645,102 710,100 L1110,96 Q1135,97 1135,122 L1135,385 Z"/>
    <path class="glass" d="M560,240 L628,178 Q640,150 660,148 L700,148 L700,240 Z"/>
    <line class="seam" x1="640" y1="130" x2="1135" y2="130"/>
    <line class="seam" x1="700" y1="200" x2="1135" y2="200"/>
    <line class="seam" x1="700" y1="300" x2="1135" y2="300"/>
    <line class="seam" x1="720" y1="150" x2="720" y2="340"/>
    <rect class="trim" x="470" y="340" width="665" height="14"/>
    <rect class="trim" x="462" y="325" width="60" height="40" rx="8"/>
    <rect class="tail-light" x="1127" y="270" width="10" height="50"/>

    <circle cx="760" cy="140" r="13" fill="none" stroke="var(--ink-brown)" stroke-width="2.5"/>
    <path d="M754,134 q0,12 12,12 l2,-3 -4,-3 -2,2 q-4,-2 -5,-5 l2,-2 -3,-4 z" fill="var(--ink-brown)"/>
    <text class="contact" x="785" y="150" font-size="30">0913 - 72 15 904</text>

    <rect x="772" y="180" width="40" height="40" fill="var(--ink-brown)"/>
    <text class="brand-name" x="826" y="204" font-size="24" letter-spacing="9">DIELEN</text>
    <text class="brand-name" x="824" y="250" font-size="46" letter-spacing="2">WARNKE</text>
    <text class="tagline" x="1085" y="288" font-size="28" text-anchor="end">BIRCH TO WENGE</text>
    <text class="tagline" x="1085" y="325" font-size="19" text-anchor="end">OVER 25 YEARS EXPERIENCE</text>

    <circle class="social-dot" cx="610" cy="300" r="11"/>
    <circle class="social-dot" cx="640" cy="300" r="11"/>
    <circle class="social-dot" cx="670" cy="300" r="11"/>

    <text class="contact" x="815" y="376" font-size="16" text-anchor="middle">WWW.DIELEN-WARNKE.EXAMPLE</text>

    <circle cx="600" cy="382" r="36" fill="var(--tyre)"/>
    <circle cx="600" cy="382" r="18" fill="var(--hub)"/>
    <circle cx="1030" cy="382" r="36" fill="var(--tyre)"/>
    <circle cx="1030" cy="382" r="18" fill="var(--hub)"/>
  </g>

  <!-- Rear doors panel -->
  <g class="panel-rear">
    <path role="img" aria-label="Holzdielen-Optik als Fahrzeugfolie" fill="url(#wood)" d="M465,760 L465,480 Q468,445 500,442 L700,442 Q732,445 735,480 L735,760 Z"/>
    <line x1="600" y1="442" x2="600" y2="740" stroke="var(--wood-dark)" stroke-width="1.5"/>
    <line class="seam" x1="465" y1="540" x2="735" y2="540"/>
    <line class="seam" x1="465" y1="610" x2="735" y2="610"/>
    <line class="seam" x1="465" y1="680" x2="735" y2="680"/>
    <rect class="tail-light" x="455" y="600" width="12" height="70" rx="2"/>
    <rect class="tail-light" x="733" y="600" width="12" height="70" rx="2"/>
    <rect class="tail-light" x="585" y="444" width="30" height="6"/>

    <rect x="490" y="478" width="32" height="32" fill="var(--ink-brown)"/>
    <text class="brand-name" x="534" y="496" font-size="18" letter-spacing="6">DIELEN</text>
    <text class="brand-name" x="532" y="530" font-size="34" letter-spacing="1">WARNKE</text>
    <text class="tagline" x="600" y="560" font-size="19" text-anchor="middle">BIRCH TO WENGE</text>
    <text class="tagline" x="600" y="588" font-size="13" text-anchor="middle">OVER 25 YEARS EXPERIENCE</text>

    <circle cx="496" cy="626" r="9" fill="none" stroke="var(--ink-brown)" stroke-width="2"/>
    <path d="M492,622 q0,8 8,8 l1.5,-2 -3,-2 -1.5,1.5 q-3,-1.5 -3.5,-3.5 l1.5,-1.5 -2,-3 z" fill="var(--ink-brown)"/>
    <text class="contact" x="512" y="633" font-size="19" letter-spacing="1">0913 - 72 15 904</text>

    <circle class="social-dot" cx="500" cy="660" r="8"/>
    <circle class="social-dot" cx="522" cy="660" r="8"/>
    <circle class="social-dot" cx="544" cy="660" r="8"/>
    <rect class="trim" x="612" y="652" width="26" height="5" rx="2"/>

    <text class="contact" x="600" y="700" font-size="12" text-anchor="middle" letter-spacing="1">WWW.DIELEN-WARNKE.EXAMPLE</text>
    <rect class="trim" x="495" y="712" width="110" height="10" rx="2"/>
    <rect class="trim" x="465" y="740" width="270" height="28" rx="4"/>
  </g>
</svg>
</body>
</html>
```